Educational Management System User Interface (Vantro Design Concepts)

Hi,I require a 1-page design for an educational management system. The image attached shows all required elements and also their locations. I require the design to be based on vantro-styled interfaces using elements from: http://qelvo.hostrun.io/qelvo-kitset/ & http://layoutmintly.com/layout-template/admin . Side menu's should not be too large that they hide the main content of the page.
Sorry very slight addition to the design as per new uploaded file.
I like how the elements of the vantro hub page are seperated with the background colour and white boxes. This could maybe work in the design as per the uploaded image?
Thanks,
Melvin
Reason: Some designers have some submissions.

```html
<!DOCTYPE html>
<html lang="en">
<head>
<meta charset="utf-8">
<title>TQ LMS – Teacher Dashboard</title>
<link href="https://fonts.googleapis.com/css2?family=Nunito+Sans:wght@300;400;600;700&display=swap" rel="stylesheet">
<style>
:root{
  --black:#000;
  --panel:#1b1b1b;
  --line:#2e2e2e;
  --teal:#1f9fb0;
  --slate:#4a6262;
  --green:#8cc63f;
  --green-btn:#7fc241;
  --grey-btn:#4a4a4a;
  --blue:#2f62a5;
  --red:#e5353f;
  --orange:#f4582b;
  --avatar-orange:#f7843f;
  --submit:#17a8a0;
  --reply:#2aa8c8;
  --text:#333;
  --muted:#777;
  --border:#d9d9d9;
}
*{box-sizing:border-box;margin:0;padding:0}
html,body{width:1200px;height:1006px;overflow:hidden;background:#fff;font-family:"Nunito Sans",Arial,sans-serif;color:var(--text)}
.canvas{position:relative;width:1200px;height:1006px}
.abs{position:absolute}

/* header */
.topbar{left:0;top:0;width:1200px;height:91px;background:var(--black)}
.brand{left:88px;top:25px;display:flex;align-items:center;gap:14px;color:#fff;font-size:26px;font-weight:400}
.brand-dot{width:40px;height:40px;border-radius:50%;background:var(--green)}
.nav-icon{top:32px;width:26px;height:26px}
.nav-sep{top:20px;width:1px;height:46px;background:#2c2c2c}
.user{left:998px;top:30px;display:flex;align-items:center;gap:10px;color:#ddd;font-size:12px;line-height:14px}
.user-ring{width:32px;height:32px;border:2px solid #ddd;border-radius:50%;display:flex;align-items:center;justify-content:center}

/* left sidebar */
.sidebar{left:60px;top:91px;width:205px;height:915px;background:var(--black)}
.side-head{height:55px;background:var(--teal);color:#fff;font-size:20px;display:flex;align-items:center;justify-content:center}
.side-sub{height:46px;background:var(--slate);color:#fff;font-size:16px;display:flex;align-items:center;padding-left:30px;gap:10px}
.group-row{height:41px;background:var(--panel);border-bottom:1px solid #000;color:#fff;font-size:13px;display:flex;align-items:center;justify-content:space-between;padding:0 22px 0 28px}
.btn{display:block;margin-left:28px;width:146px;height:31px;color:#fff;font-size:13.5px;text-align:center;line-height:31px;border-radius:2px}
.btn-create{background:var(--green-btn);margin-top:8px}
.btn-join{background:var(--grey-btn);margin-top:6px}
.community{margin-top:14px;height:39px;background:var(--blue);color:#fff;font-size:14px;display:flex;align-items:center;justify-content:center}
.community-row{height:41px;font-size:14px}

/* main feed */
.refine{left:697px;top:103px;width:158px;height:26px;background:#e4e4e4;border-radius:2px;font-size:13.5px;display:flex;align-items:center;justify-content:space-between;padding:0 9px 0 16px}
.avatar{border-radius:50%;display:flex;align-items:center;justify-content:center}
.post-input{left:353px;top:152px;width:501px;height:52px;border:1px solid var(--border);font-size:12.5px;padding:18px 0 0 20px}
.submit{left:763px;top:211px;width:91px;height:27px;background:var(--submit);color:#222;font-size:13.5px;text-align:center;line-height:27px}
.timeline{left:311px;top:277px;width:1px;height:692px;background:#bcbcbc}
.card{border:1px solid var(--border);background:#fff}
.card-head{display:flex;align-items:baseline;gap:14px;color:#555}
.card-name{font-size:19px;font-weight:300}
.card-meta{font-size:14px;font-weight:300}
.card-body{font-size:11.5px;line-height:14.5px;color:#333;margin-top:8px}
.reply{position:absolute;right:10px;bottom:12px;width:22px;height:18px}
.file-icon{width:52px;height:52px;background:#c8141e;border-radius:6px}
.file-name{font-size:11.5px;color:#c8141e;margin-top:4px}

/* right panel */
.events{left:874px;top:91px;width:266px;height:915px;background:var(--black)}
.event-head{height:55px;color:#fff;font-size:20px;display:flex;align-items:center;justify-content:center;gap:12px}
.event-head.today{background:var(--red)}
.event-head.upcoming{background:var(--orange)}
.event-row{height:55.4px;background:var(--panel);border-bottom:1px solid #0c0c0c;color:#eee;font-size:13.5px;display:flex;align-items:center;justify-content:space-between;padding:0 12px 0 18px}
.info{width:16px;height:16px;border-radius:50%;background:#8a8a8a;color:var(--panel);font-size:11px;font-weight:700;text-align:center;line-height:16px;font-style:italic}
.footer{left:936px;top:965px;color:#fff;font-size:13px}
.page-tag{left:1161px;top:966px;font-size:11px;color:#222}
</style>
</head>
<body>
<div class="canvas">

  <!-- header -->
  <header class="abs topbar">
    <div class="abs brand"><span class="brand-dot"></span>TQ LMS</div>

    <svg class="abs nav-icon" style="left:346px" viewBox="0 0 24 24"><path d="M12 3 2 12h3v8h5v-5h4v5h5v-8h3z" fill="#4aa3df"/></svg>
    <div class="abs nav-sep" style="left:389px"></div>
    <svg class="abs nav-icon" style="left:412px" viewBox="0 0 24 24"><rect x="3" y="5" width="18" height="16" fill="none" stroke="#e5353f" stroke-width="2"/><rect x="3" y="5" width="18" height="5" fill="#e5353f"/><path d="M7 2v5M17 2v5M6 13h12M6 17h12M10 10v10M14 10v10" stroke="#e5353f" stroke-width="1.6"/></svg>
    <div class="abs nav-sep" style="left:458px"></div>
    <svg class="abs nav-icon" style="left:478px" viewBox="0 0 24 24"><path d="M3 13l6 6L21 6" fill="none" stroke="#6cc04a" stroke-width="4"/></svg>
    <div class="abs nav-sep" style="left:523px"></div>
    <svg class="abs nav-icon" style="left:544px" viewBox="0 0 24 24"><path d="M2 6h7l2 2h9v3H6l-4 9z" fill="#f0a030"/><path d="M6 11h17l-4 9H2z" fill="#f6b24a"/></svg>
    <div class="abs nav-sep" style="left:590px"></div>

    <div class="abs nav-sep" style="left:837px"></div>
    <svg class="abs nav-icon" style="left:860px" viewBox="0 0 24 24"><rect x="1" y="5" width="22" height="15" rx="2" fill="#ccc"/><path d="M1 7l11 7 11-7" fill="none" stroke="#000" stroke-width="1.6"/></svg>
    <div class="abs nav-sep" style="left:905px"></div>
    <svg class="abs nav-icon" style="left:927px" viewBox="0 0 24 24"><circle cx="12" cy="12" r="10" fill="#ccc"/><path d="M8 8l8 8M16 8l-8 8" stroke="#000" stroke-width="3"/></svg>
    <div class="abs nav-sep" style="left:971px"></div>

    <div class="abs user">
      <span class="user-ring"><svg width="18" height="18" viewBox="0 0 24 24"><circle cx="12" cy="8" r="5" fill="#ddd"/><path d="M3 22c0-6 4-9 9-9s9 3 9 9z" fill="#ddd"/></svg></span>
      <span>Marta<br>Quillon</span>
    </div>
  </header>

  <!-- left sidebar -->
  <aside class="abs sidebar">
    <div class="side-head">TEACHERS</div>
    <div class="side-sub">
      <svg width="26" height="22" viewBox="0 0 26 22"><circle cx="13" cy="6" r="4" fill="#fff"/><circle cx="5" cy="8" r="3" fill="#fff"/><circle cx="21" cy="8" r="3" fill="#fff"/><path d="M6 20c0-5 3-8 7-8s7 3 7 8zM0 18c0-4 2-6 5-6s4 1 4 2c-2 1-3 3-3 4zM26 18c0-4-2-6-5-6s-4 1-4 2c2 1 3 3 3 4z" fill="#fff"/></svg>
      MY GROUPS
    </div>
    <div class="group-row">Group Name 1<svg width="8" height="12" viewBox="0 0 8 12"><path d="M1 1l5 5-5 5" fill="none" stroke="#fff" stroke-width="2.4"/></svg></div>
    <div class="group-row">Group Name 2<svg width="8" height="12" viewBox="0 0 8 12"><path d="M1 1l5 5-5 5" fill="none" stroke="#fff" stroke-width="2.4"/></svg></div>
    <div class="group-row">Group Name 3<svg width="8" height="12" viewBox="0 0 8 12"><path d="M1 1l5 5-5 5" fill="none" stroke="#fff" stroke-width="2.4"/></svg></div>
    <div class="group-row">Group Name 4<svg width="8" height="12" viewBox="0 0 8 12"><path d="M1 1l5 5-5 5" fill="none" stroke="#fff" stroke-width="2.4"/></svg></div>
    <span class="btn btn-create">CREATE NEW GROUP</span>
    <span class="btn btn-join">JOIN MORE GROUP</span>
    <div class="community">COMMUNITY</div>
    <div class="group-row community-row">Study Finch<svg width="8" height="12" viewBox="0 0 8 12"><path d="M1 1l5 5-5 5" fill="none" stroke="#fff" stroke-width="2.4"/></svg></div>
  </aside>

  <!-- main feed -->
  <main>
    <div class="abs refine">Refine by group
      <svg width="14" height="14" viewBox="0 0 14 14"><circle cx="7" cy="7" r="7" fill="#111"/><path d="M4 6l3 3 3-3" fill="none" stroke="#fff" stroke-width="1.8"/></svg>
    </div>

    <div class="abs avatar" style="left:284px;top:150px;width:56px;height:56px;background:var(--avatar-orange)">
      <svg width="28" height="28" viewBox="0 0 24 24"><circle cx="12" cy="7" r="5" fill="#fff"/><path d="M2 23c0-7 4-10 10-10s10 3 10 10z" fill="#fff"/></svg>
    </div>
    <div class="abs post-input">Please post your update</div>

    <svg class="abs" style="left:646px;top:214px" width="22" height="22" viewBox="0 0 22 22"><g fill="none" stroke="#888" stroke-width="2"><circle cx="7" cy="7" r="4"/><circle cx="15" cy="15" r="4"/><path d="M9 9l4 4"/></g></svg>
    <svg class="abs" style="left:686px;top:212px" width="20" height="24" viewBox="0 0 20 24"><path d="M2 1h11l5 5v17H2z" fill="none" stroke="#888" stroke-width="1.6"/><path d="M5 11h10M5 14h10M5 17h10" stroke="#888" stroke-width="1.3"/></svg>
    <svg class="abs" style="left:721px;top:214px" width="24" height="20" viewBox="0 0 24 20"><rect x="1" y="3" width="22" height="16" fill="none" stroke="#888" stroke-width="1.8"/><rect x="1" y="3" width="22" height="4" fill="#888"/><circle cx="12" cy="12" r="4" fill="none" stroke="#888" stroke-width="1.8"/></svg>
    <div class="abs submit">Submit</div>

    <svg class="abs" style="left:298px;top:262px" width="30" height="32" viewBox="0 0 30 32"><path d="M23 10a11 11 0 1 1-8-4" fill="none" stroke="#8cc63f" stroke-width="3.4"/><path d="M11 1l7 5-6 5z" fill="#8cc63f"/></svg>
    <div class="abs timeline"></div>

    <!-- post 1 -->
    <div class="abs avatar" style="left:284px;top:342px;width:56px;height:56px;background:var(--green)"><svg width="28" height="28" viewBox="0 0 24 24"><circle cx="12" cy="7" r="5" fill="#fff"/><path d="M2 23c0-7 4-10 10-10s10 3 10 10z" fill="#fff"/></svg></div>
    <article class="abs card" style="left:353px;top:292px;width:501px;height:133px;padding:14px 12px 0 12px">
      <div class="card-head"><span class="card-name">Dorian Pelley</span><span class="card-meta">|&nbsp;&nbsp;&nbsp;&nbsp;9:15&nbsp;&nbsp;&nbsp;&nbsp;14-05-2014</span></div>
      <p class="card-body">Neque porro quisquam est, qui dolorem ipsum quia dolor sit amet, consectetur, adipisci velit, sed quia non numquam eius modi tempora incidunt ut labore et dolore magnam aliquam quaerat voluptatem. Ut enim ad minima veniam, quis nostrum exercitationem ullam corporis suscipit</p>
      <svg class="reply" viewBox="0 0 22 18"><path d="M9 1 1 8l8 7v-4c6 0 10 1 12 6 0-7-4-11-12-11z" fill="var(--reply)"/></svg>
    </article>

    <!-- post 2 -->
    <div class="abs avatar" style="left:284px;top:491px;width:56px;height:56px;background:var(--green)"><svg width="28" height="28" viewBox="0 0 24 24"><circle cx="12" cy="7" r="5" fill="#fff"/><path d="M2 23c0-7 4-10 10-10s10 3 10 10z" fill="#fff"/></svg></div>
    <article class="abs card" style="left:353px;top:440px;width:501px;height:134px;padding:14px 12px 0 12px">
      <div class="card-head"><span class="card-name">Dorian Pelley</span><span class="card-meta">|&nbsp;&nbsp;&nbsp;&nbsp;9:15&nbsp;&nbsp;&nbsp;&nbsp;14-05-2014</span></div>
      <p class="card-body">Neque porro quisquam est, qui dolorem ipsum quia dolor sit amet, consectetur, adipisci velit, sed quia non numquam eius modi tempora incidunt ut labore et dolore magnam aliquam quaerat voluptatem. Ut enim ad minima veniam, quis nostrum exercitationem ullam corporis suscipit</p>
      <svg class="reply" viewBox="0 0 22 18"><path d="M9 1 1 8l8 7v-4c6 0 10 1 12 6 0-7-4-11-12-11z" fill="var(--reply)"/></svg>
    </article>

    <!-- post 3 with attachment -->
    <div class="abs avatar" style="left:284px;top:638px;width:56px;height:56px;background:var(--green)"><svg width="28" height="28" viewBox="0 0 24 24"><circle cx="12" cy="7" r="5" fill="#fff"/><path d="M2 23c0-7 4-10 10-10s10 3 10 10z" fill="#fff"/></svg></div>
    <article class="abs card" style="left:353px;top:589px;width:501px;height:134px">
      <div class="abs" style="left:16px;top:34px;text-align:center">
        <div class="file-icon" style="margin-left:2px"></div>
        <div class="file-name">Results.pdf</div>
      </div>
      <div class="abs" style="left:85px;top:14px;width:405px">
        <div class="card-head"><span class="card-name">Dorian Pelley</span><span class="card-meta">|&nbsp;&nbsp;&nbsp;&nbsp;9:15&nbsp;&nbsp;&nbsp;&nbsp;14-05-2014</span></div>
        <p class="card-body">Neque porro quisquam est, qui dolorem ipsum quia dolor sit amet, consectetur, adipisci velit, sed quia non numquam eius modi tempora incidunt ut labore et dolore magnam aliquam quaerat voluptatem. Ut enim ad minima veniam, quis nostrum exercitationem ullam corporis suscipit</p>
      </div>
      <svg class="reply" viewBox="0 0 22 18"><path d="M9 1 1 8l8 7v-4c6 0 10 1 12 6 0-7-4-11-12-11z" fill="var(--reply)"/></svg>
    </article>

    <!-- reply -->
    <div class="abs" style="left:388px;top:723px;width:1px;height:49px;background:#bcbcbc"></div>
    <div class="abs" style="left:388px;top:772px;width:48px;height:1px;background:#bcbcbc"></div>
    <div class="abs avatar" style="left:359px;top:743px;width:56px;height:56px;background:#a6a6a6"><svg width="28" height="28" viewBox="0 0 24 24"><circle cx="12" cy="7" r="5" fill="#fff"/><path d="M2 23c0-7 4-10 10-10s10 3 10 10z" fill="#fff"/></svg></div>
    <article class="abs card" style="left:436px;top:733px;width:418px;height:88px;padding:24px 18px 0 18px">
      <div class="card-head"><span class="card-name" style="font-size:16.5px;color:#888">Reuben Alcott</span><span class="card-meta" style="font-size:12px">|&nbsp;&nbsp;&nbsp;&nbsp;9:15&nbsp;&nbsp;&nbsp;&nbsp;14-05-2014</span></div>
      <p class="card-body" style="margin-top:6px">Thanks for this, Very helpfull</p>
      <svg class="reply" viewBox="0 0 22 18"><path d="M9 1 1 8l8 7v-4c6 0 10 1 12 6 0-7-4-11-12-11z" fill="var(--reply)"/></svg>
    </article>

    <!-- post 4 -->
    <div class="abs avatar" style="left:284px;top:880px;width:56px;height:56px;background:var(--green)"><svg width="28" height="28" viewBox="0 0 24 24"><circle cx="12" cy="7" r="5" fill="#fff"/><path d="M2 23c0-7 4-10 10-10s10 3 10 10z" fill="#fff"/></svg></div>
    <article class="abs card" style="left:353px;top:830px;width:501px;height:134px;padding:14px 12px 0 12px">
      <div class="card-head"><span class="card-name">Dorian Pelley</span><span class="card-meta">|&nbsp;&nbsp;&nbsp;&nbsp;9:15&nbsp;&nbsp;&nbsp;&nbsp;14-05-2014</span></div>
      <p class="card-body">Neque porro quisquam est, qui dolorem ipsum quia dolor sit amet, consectetur, adipisci velit, sed quia non numquam eius modi tempora incidunt ut labore et dolore magnam aliquam quaerat voluptatem. Ut enim ad minima veniam, quis nostrum exercitationem ullam corporis suscipit</p>
    </article>
  </main>

  <!-- events panel -->
  <aside class="abs events">
    <div class="event-head today">
      <svg width="22" height="22" viewBox="0 0 24 24"><rect x="2" y="4" width="20" height="18" fill="none" stroke="#fff" stroke-width="2"/><rect x="2" y="4" width="20" height="5" fill="#fff"/><path d="M7 1v5M17 1v5M5 13h14M5 17h14M9 9v12M15 9v12" stroke="#fff" stroke-width="1.5"/></svg>
      TODAY'S EVENTS
    </div>
    <div class="event-row">12:15 am Meeting in the Canteen<span class="info">i</span></div>
    <div class="event-row">12:45 pm Assignment One is Due<span class="info">i</span></div>
    <div class="event-row">12:15 am Meeting in the Canteen<span class="info">i</span></div>
    <div class="event-row">12:45 pm Assignment One is Due<span class="info">i</span></div>
    <div class="event-row">12:15 am Meeting in the Canteen<span class="info">i</span></div>
    <div class="event-head upcoming">
      <svg width="22" height="22" viewBox="0 0 24 24"><rect x="2" y="4" width="20" height="18" fill="none" stroke="#fff" stroke-width="2"/><rect x="2" y="4" width="20" height="5" fill="#fff"/><path d="M7 1v5M17 1v5M5 13h14M5 17h14M9 9v12M15 9v12" stroke="#fff" stroke-width="1.5"/></svg>
      UPCOMING EVENTS
    </div>
    <div class="event-row">12:15 am Meeting in the Canteen<span class="info">i</span></div>
    <div class="event-row">12:45 pm Assignment One is Due<span class="info">i</span></div>
    <div class="event-row">12:15 am Meeting in the Canteen<span class="info">i</span></div>
  </aside>

  <div class="abs footer">©2014.www.tqlearning.net</div>
  <div class="abs page-tag">M1</div>
</div>
</body>
</html>
```